Halloway Crest Backers Guild business cards

Create a single-sided business card for the Halloway Crest Backers Guild based on the attached logo.
The additional data fields include Name, Title, Email, Phone, and website.
Please use the following as sample data:
Name: Dean Varrow
Title: Co-Founder / Investor
Email: deanvarrow@mailtern.net
Phone: 555-314-2706
Website: www.hcbackersguild.com

Target Market(s)

Start ups, entrepreneurs, venture capitalists

Industry/Entity Type

Investment

Contact Information for Business Card

Professional business card. Technology company.

Font styles to use
Serif
Sans Serif

Requirements
Must have
• Include the HCBG logo (attached)
• Name
• Title
• Email
• Phone
• Website
Should not have
• Cute, cartoony

```html
<!DOCTYPE html>
<html lang="en">
<head>
<meta charset="utf-8">
<title>Halloway Crest Backers Guild – Business Card</title>
<link href="https://fonts.googleapis.com/css2?family=Lato:wght@400;700;900&display=swap" rel="stylesheet">
<style>
  :root {
    --page-bg: #e9edf1;
    --card-bg: #ffffff;
    --brand-green: #1e9a4b;
    --ink-dark: #3a3a3c;
    --ink-body: #3f3f41;
    --card-shadow: rgba(30, 40, 55, 0.18);
  }
  * { margin: 0; padding: 0; box-sizing: border-box; }
  html, body {
    width: 1200px;
    height: 900px;
    overflow: hidden;
    background: var(--page-bg);
    font-family: "Lato", "Helvetica Neue", Arial, sans-serif;
  }
  .business-card {
    position: absolute;
    left: 180px;
    top: 210px;
    width: 840px;
    height: 480px;
    background: var(--card-bg);
    border-radius: 16px;
    box-shadow: 0 10px 30px var(--card-shadow);
    overflow: hidden;
  }
  .brand-lockup {
    position: absolute;
    left: 50px;
    top: 50px;
    display: flex;
    align-items: center;
    height: 112px;
  }
  .brand-mark {
    width: 56px;
    height: 56px;
    border-radius: 50%;
    background: var(--brand-green);
    margin: 0 30px 0 22px;
  }
  .brand-divider {
    width: 2px;
    height: 112px;
    background: var(--brand-green);
    margin-right: 16px;
  }
  .brand-name {
    color: var(--ink-dark);
    font-weight: 700;
    font-size: 31px;
    line-height: 38px;
    letter-spacing: 0.2px;
  }
  .contact-block {
    position: absolute;
    left: 50px;
    top: 298px;
  }
  .person-name {
    font-weight: 700;
    font-size: 22px;
    color: var(--ink-dark);
    letter-spacing: 0.4px;
    line-height: 28px;
  }
  .person-title {
    font-size: 19px;
    color: var(--brand-green);
    line-height: 26px;
    margin-bottom: 12px;
  }
  .contact-line {
    display: flex;
    align-items: center;
    font-size: 19px;
    color: var(--ink-body);
    line-height: 29px;
  }
  .contact-icon {
    width: 16px;
    height: 16px;
    margin-right: 12px;
    fill: var(--brand-green);
    flex: none;
  }
</style>
</head>
<body>
  <main class="business-card">
    <div class="brand-lockup">
      <span class="brand-mark" aria-hidden="true"></span>
      <span class="brand-divider" aria-hidden="true"></span>
      <p class="brand-name">Halloway Crest<br>Backers Guild</p>
    </div>

    <section class="contact-block">
      <h1 class="person-name">DEAN VARROW</h1>
      <p class="person-title">Co-Founder / Investor</p>
      <p class="contact-line">
        <svg class="contact-icon" viewBox="0 0 24 24" aria-hidden="true"><path d="M6.6 10.8a15.1 15.1 0 0 0 6.6 6.6l2.2-2.2c.3-.3.7-.4 1-.2 1.1.4 2.3.6 3.6.6.6 0 1 .4 1 1V20c0 .6-.4 1-1 1A17 17 0 0 1 3 4c0-.6.4-1 1-1h3.5c.6 0 1 .4 1 1 0 1.3.2 2.5.6 3.6.1.3 0 .7-.2 1z"/></svg>
        555-314-2706
      </p>
      <p class="contact-line">
        <svg class="contact-icon" viewBox="0 0 24 24" aria-hidden="true"><path d="M2 5h20v14H2zm2 2v.6l8 5.2 8-5.2V7zm0 3v7h16v-7l-8 5.2z"/></svg>
        deanvarrow@mailtern.net
      </p>
      <p class="contact-line">
        <svg class="contact-icon" viewBox="0 0 24 24" aria-hidden="true"><path d="M12 2a10 10 0 1 0 0 20 10 10 0 0 0 0-20zm6.9 9h-3a15.6 15.6 0 0 0-1.3-5.9A8 8 0 0 1 18.9 11zM12 4.1c.9 1.2 1.8 3.6 1.9 6.9h-3.8c.1-3.3 1-5.7 1.9-6.9zM9.4 5.1A15.6 15.6 0 0 0 8.1 11h-3a8 8 0 0 1 4.3-5.9zM5.1 13h3a15.6 15.6 0 0 0 1.3 5.9A8 8 0 0 1 5.1 13zm6.9 6.9c-.9-1.2-1.8-3.6-1.9-6.9h3.8c-.1 3.3-1 5.7-1.9 6.9zm2.6-1A15.6 15.6 0 0 0 15.9 13h3a8 8 0 0 1-4.3 5.9z"/></svg>
        www.hcbackersguild.com
      </p>
    </section>
  </main>
</body>
</html>
```